Restaurant promotion flyer

I am selling restaurant thermal paper, pizza boxes, show-up: Order online local delivery, Competitive price,

Target Market(s)

Restaurants

Industry/Entity Type

Restaurant supplies

Requirements
Must have
• The flyers should have headers saying local, the pictures of the items we are selling, and the pricing right next to each of them. The flyer should also be attractive to customers.
Nice to have
• Somethings nice is can show how low and good the pricing is for the products.
Should not have
• Receipt Paper $45.00 3-1/8x230-50 R ; $35.00 3-1/8X119-50 R; Credit Card Paper $26.00 2-1/4x50-100 R; $16.00 2-1/4x85-50 R; Pump Gas Station: $31.00 2-5/16x356-24 R ; $ 25.00 2-5/16X210-24 R;

```html
<!DOCTYPE html>
<html lang="en">
<head>
<meta charset="utf-8">
<title>Restaurant Supplies Flyer</title>
<link rel="stylesheet" href="https://fonts.googleapis.com/css2?family=Montserrat:wght@800;900&family=Open+Sans:wght@400;600;700;800&family=Saira+Condensed:wght@800&display=swap">
<style>
  :root {
    --blue: #0e4fa3;
    --navy: #0f1f3f;
    --green: #22ff00;
    --red: #e21b23;
    --ink: #111111;
    --paper: #ffffff;
    --stage: #f2f2f2;
    --kraft-light: #d6ac72;
    --kraft-dark: #a87945;
    --label-light: #f4f4f2;
    --label-dark: #c9c9c6;
    --cup-light: #fbfaf6;
    --cup-dark: #dcd8cf;
  }
  * { box-sizing: border-box; margin: 0; padding: 0; }
  html, body { width: 1200px; height: 1200px; overflow: hidden; background: var(--stage); }
  .flyer {
    position: absolute; left: 159px; top: 30px;
    width: 1114px; height: 1440px;
    transform: scale(0.7917); transform-origin: top left;
    background: var(--paper);
    font-family: "Open Sans", sans-serif; color: var(--ink);
    overflow: hidden;
  }
  .masthead {
    position: absolute; left: 0; top: 0; width: 100%; height: 320px;
    background: var(--blue); color: #fff; text-align: center;
  }
  .masthead__title {
    position: absolute; left: 0; right: 0; top: 44px;
    font-family: "Montserrat", sans-serif; font-weight: 900;
    font-size: 124px; line-height: 1; letter-spacing: 2px;
  }
  .masthead__subtitle {
    position: absolute; left: 0; right: 0; top: 162px;
    font-family: "Montserrat", sans-serif; font-weight: 900;
    font-size: 72px; line-height: 1; letter-spacing: 1px;
  }
  .masthead__tagline {
    position: absolute; left: 0; right: 0; top: 236px;
    font-weight: 700; font-size: 25px;
  }
  .ribbon { position: absolute; left: 0; top: 320px; width: 100%; height: 70px; }
  .ribbon svg { position: absolute; inset: 0; }
  .ribbon__local {
    position: absolute; left: 16px; top: 8px; width: 270px;
    font-family: "Saira Condensed", sans-serif; font-weight: 800;
    font-size: 24px; line-height: 27px; white-space: nowrap;
    color: var(--navy); transform: skewX(-12deg);
  }
  .ribbon__headline {
    position: absolute; left: 330px; right: 14px; top: 16px;
    font-family: "Montserrat", sans-serif; font-weight: 800; font-size: 29px;
    color: #fff; letter-spacing: 1px; white-space: nowrap;
  }
  .products {
    position: absolute; left: 30px; top: 422px;
    display: grid; grid-template-columns: 369px 373px 330px;
    grid-auto-rows: 232px;
  }
  .product { position: relative; }
  .product__photo { position: absolute; left: 182px; top: 30px; width: 150px; height: 150px; border-radius: 6px; }
  .photo--labels { background: linear-gradient(135deg, var(--label-light), var(--label-dark)); }
  .photo--pizza { background: linear-gradient(135deg, var(--kraft-light), var(--kraft-dark)); }
  .photo--cups { background: linear-gradient(135deg, var(--cup-light), var(--cup-dark)); }
  .product__text { position: relative; z-index: 1; width: 176px; }
  .badge {
    display: inline-block; background: var(--red); color: #fff;
    font-weight: 600; font-size: 15px; line-height: 20px; padding: 0 4px;
  }
  .price { display: flex; align-items: flex-start; font-weight: 800; line-height: 1; margin-top: 2px; }
  .price__currency { font-size: 20px; margin-top: 4px; }
  .price__whole { font-size: 48px; letter-spacing: -1px; }
  .price__cents { font-size: 24px; margin-top: 2px; }
  .price__note { font-size: 13px; letter-spacing: -0.3px; margin-top: -2px; }
  .product__name { font-weight: 700; font-size: 21px; line-height: 1; margin-top: 12px; white-space: nowrap; }
  .product__sub { font-weight: 800; font-size: 15px; line-height: 1; }
  .product__desc { font-size: 13.5px; line-height: 13px; margin-top: 3px; white-space: nowrap; }
  .footer { position: absolute; left: 0; top: 1340px; width: 100%; height: 100px; }
  .brand {
    position: absolute; left: 34px; top: 24px; display: flex; align-items: center; gap: 12px;
    font-family: "Open Sans", sans-serif; font-weight: 800; font-size: 44px; color: var(--blue);
  }
  .brand__dot { width: 40px; height: 40px; border-radius: 50%; background: var(--blue); }
  .footer__rule { position: absolute; left: 359px; top: 0; width: 7px; height: 100px; background: var(--blue); }
  .footer__panel {
    position: absolute; left: 373px; top: 0; right: 0; height: 100px;
    background: var(--blue); color: #fff; padding: 10px 0 0 34px;
  }
  .footer__lead { font-weight: 700; font-size: 20px; line-height: 26px; }
  .footer__sub { font-weight: 600; font-size: 20px; line-height: 28px; }
  .footer__note { font-size: 16px; line-height: 24px; }
</style>
</head>
<body>
<main class="flyer">
  <header class="masthead">
    <h1 class="masthead__title">LOREM IPSUM</h1>
    <h2 class="masthead__subtitle">CONSECTETUR ADIPISCING</h2>
    <p class="masthead__tagline">LOREM IPSUM DOLOR SIT AMET, CONSECTETUR ADIPISCING ELIT</p>
  </header>

  <section class="ribbon">
    <svg width="1114" height="70" viewBox="0 0 1114 70" aria-hidden="true">
      <polygon points="0,0 309,0 291,70 0,70" fill="var(--green)"/>
      <polygon points="318,0 1114,0 1114,70 300,70" fill="var(--navy)"/>
    </svg>
    <p class="ribbon__local">LOREM IPSUM<br>CONSECTETUR ADIPISCING ELIT</p>
    <p class="ribbon__headline">LOREM IPSUM CONSECTETUR ADIPISCING ELIT</p>
  </section>

  <section class="products">
    <article class="product"><div class="product__photo photo--labels" role="img" aria-label="Rolls of thermal receipt labels"></div><div class="product__text"><span class="badge">QUALIFIED</span><div class="price"><span class="price__currency">$</span><span class="price__whole">00</span><span class="price__cents">00</span></div><p class="price__note">best prices</p><p class="product__name">LOREM IPSUM</p><p class="product__sub">DOLOR SIT AMET,</p><p class="product__desc">consectetur adipiscing elit,<br>sed do eiusmod tempor<br>incididunt ut<br>labore et dolore<br>magna aliqua.</p></div></article>
    <article class="product"><div class="product__photo photo--pizza" role="img" aria-label="Open kraft pizza box"></div><div class="product__text"><span class="badge">QUALIFIED</span><div class="price"><span class="price__currency">$</span><span class="price__whole">00</span><span class="price__cents">00</span></div><p class="price__note">best prices</p><p class="product__name">LOREM IPSUM</p><p class="product__sub">DOLOR SIT AMET,</p><p class="product__desc">consectetur adipiscing elit,<br>sed do eiusmod tempor<br>incididunt ut<br>labore et dolore<br>magna aliqua.</p></div></article>
    <article class="product"><div class="product__photo photo--cups" role="img" aria-label="White paper cups with lids"></div><div class="product__text"><span class="badge">QUALIFIED</span><div class="price"><span class="price__currency">$</span><span class="price__whole">00</span><span class="price__cents">00</span></div><p class="price__note">best prices</p><p class="product__name">LOREM IPSUM</p><p class="product__sub">DOLOR SIT AMET,</p><p class="product__desc">consectetur adipiscing elit,<br>sed do eiusmod tempor<br>incididunt ut<br>labore et dolore<br>magna aliqua.</p></div></article>

    <article class="product"><div class="product__photo photo--pizza" role="img" aria-label="Open kraft pizza box"></div><div class="product__text"><span class="badge">QUALIFIED</span><div class="price"><span class="price__currency">$</span><span class="price__whole">00</span><span class="price__cents">00</span></div><p class="price__note">best prices</p><p class="product__name">LOREM IPSUM</p><p class="product__sub">DOLOR SIT AMET,</p><p class="product__desc">consectetur adipiscing elit,<br>sed do eiusmod tempor<br>incididunt ut<br>labore et dolore<br>magna aliqua.</p></div></article>
    <article class="product"><div class="product__photo photo--cups" role="img" aria-label="White paper cups with lids"></div><div class="product__text"><span class="badge">QUALIFIED</span><div class="price"><span class="price__currency">$</span><span class="price__whole">00</span><span class="price__cents">00</span></div><p class="price__note">best prices</p><p class="product__name">LOREM IPSUM</p><p class="product__sub">DOLOR SIT AMET,</p><p class="product__desc">consectetur adipiscing elit,<br>sed do eiusmod tempor<br>incididunt ut<br>labore et dolore<br>magna aliqua.</p></div></article>
    <article class="product"><div class="product__photo photo--labels" role="img" aria-label="Rolls of thermal receipt labels"></div><div class="product__text"><span class="badge">QUALIFIED</span><div class="price"><span class="price__currency">$</span><span class="price__whole">00</span><span class="price__cents">00</span></div><p class="price__note">best prices</p><p class="product__name">LOREM IPSUM</p><p class="product__sub">DOLOR SIT AMET,</p><p class="product__desc">consectetur adipiscing elit,<br>sed do eiusmod tempor<br>incididunt ut<br>labore et dolore<br>magna aliqua.</p></div></article>

    <article class="product"><div class="product__photo photo--cups" role="img" aria-label="White paper cups with lids"></div><div class="product__text"><span class="badge">QUALIFIED</span><div class="price"><span class="price__currency">$</span><span class="price__whole">00</span><span class="price__cents">00</span></div><p class="price__note">best prices</p><p class="product__name">LOREM IPSUM</p><p class="product__sub">DOLOR SIT AMET,</p><p class="product__desc">consectetur adipiscing elit,<br>sed do eiusmod tempor<br>incididunt ut<br>labore et dolore<br>magna aliqua.</p></div></article>
    <article class="product"><div class="product__photo photo--labels" role="img" aria-label="Rolls of thermal receipt labels"></div><div class="product__text"><span class="badge">QUALIFIED</span><div class="price"><span class="price__currency">$</span><span class="price__whole">00</span><span class="price__cents">00</span></div><p class="price__note">best prices</p><p class="product__name">LOREM IPSUM</p><p class="product__sub">DOLOR SIT AMET,</p><p class="product__desc">consectetur adipiscing elit,<br>sed do eiusmod tempor<br>incididunt ut<br>labore et dolore<br>magna aliqua.</p></div></article>
    <article class="product"><div class="product__photo photo--pizza" role="img" aria-label="Open kraft pizza box"></div><div class="product__text"><span class="badge">QUALIFIED</span><div class="price"><span class="price__currency">$</span><span class="price__whole">00</span><span class="price__cents">00</span></div><p class="price__note">best prices</p><p class="product__name">LOREM IPSUM</p><p class="product__sub">DOLOR SIT AMET,</p><p class="product__desc">consectetur adipiscing elit,<br>sed do eiusmod tempor<br>incididunt ut<br>labore et dolore<br>magna aliqua.</p></div></article>

    <article class="product"><div class="product__photo photo--labels" role="img" aria-label="Rolls of thermal receipt labels"></div><div class="product__text"><span class="badge">QUALIFIED</span><div class="price"><span class="price__currency">$</span><span class="price__whole">00</span><span class="price__cents">00</span></div><p class="price__note">best prices</p><p class="product__name">LOREM IPSUM</p><p class="product__sub">DOLOR SIT AMET,</p><p class="product__desc">consectetur adipiscing elit,<br>sed do eiusmod tempor<br>incididunt ut<br>labore et dolore<br>magna aliqua.</p></div></article>
    <article class="product"><div class="product__photo photo--pizza" role="img" aria-label="Open kraft pizza box"></div><div class="product__text"><span class="badge">QUALIFIED</span><div class="price"><span class="price__currency">$</span><span class="price__whole">00</span><span class="price__cents">00</span></div><p class="price__note">best prices</p><p class="product__name">LOREM IPSUM</p><p class="product__sub">DOLOR SIT AMET,</p><p class="product__desc">consectetur adipiscing elit,<br>sed do eiusmod tempor<br>incididunt ut<br>labore et dolore<br>magna aliqua.</p></div></article>
    <article class="product"><div class="product__photo photo--labels" role="img" aria-label="Rolls of thermal receipt labels"></div><div class="product__text"><span class="badge">QUALIFIED</span><div class="price"><span class="price__currency">$</span><span class="price__whole">00</span><span class="price__cents">00</span></div><p class="price__note">best prices</p><p class="product__name">LOREM IPSUM</p><p class="product__sub">DOLOR SIT AMET,</p><p class="product__desc">consectetur adipiscing elit,<br>sed do eiusmod tempor<br>incididunt ut<br>labore et dolore<br>magna aliqua.</p></div></article>
  </section>

  <footer class="footer">
    <div class="brand"><span class="brand__dot"></span><span>Tablora</span></div>
    <div class="footer__rule"></div>
    <div class="footer__panel">
      <p class="footer__lead">LOREM IPSUM DOLOR SIT AMET,</p>
      <p class="footer__sub">consectetur adipiscing elit, sed do eiusmod tempor incididunt ut</p>
      <p class="footer__note">labore et dolore magna aliqua. Ut enim ad minim veniam,</p>
    </div>
  </footer>
</main>
</body>
</html>
```